Bakery Business Cards

We are in need of business cards for our bakery business--something non-generic that reflects our business and will stand out. We are a wholesale bakery that primarily services in-store bakeries, casinos, schools, distributors, and fund-raising companies. The family business was founded in 1960. (www.marlowsovenworks.com)

```html
<!DOCTYPE html>
<html lang="en">
<head>
<meta charset="utf-8">
<title>Marlow's Ovenworks – Business Card</title>
<link rel="stylesheet" href="https://fonts.googleapis.com/css2?family=Open+Sans:ital,wght@0,400;0,700;1,400&display=swap">
<style>
  :root {
    --stage: #2a2a2c;
    --card-white: #ffffff;
    --brand-blue: #3a63c4;
    --blue-light: #4d74c9;
    --blue-deep: #1c3f9e;
    --text-grey: #7a7a7a;
    --icon-blue: #3a63c4;
  }
  * { box-sizing: border-box; margin: 0; padding: 0; }
  html, body {
    width: 1200px; height: 900px; overflow: hidden;
    background: var(--stage);
    font-family: "Open Sans", Arial, sans-serif;
  }
  .sheet {
    width: 1200px; height: 900px;
    display: flex; flex-direction: column; align-items: center; justify-content: center;
    gap: 40px;
  }
  .card {
    width: 700px; height: 400px; position: relative;
    box-shadow: 0 10px 30px rgba(0,0,0,.45);
  }
  .card-front { background: var(--card-white); }
  .card-back {
    background: radial-gradient(ellipse at 40% 40%, var(--blue-light) 0%, var(--blue-deep) 100%);
    display: flex; align-items: center; justify-content: center;
  }
  .identity { position: absolute; left: 50px; top: 50px; }
  .person-name {
    color: var(--brand-blue); font-weight: 700; font-size: 22px;
    text-transform: uppercase; letter-spacing: .2px;
  }
  .person-role { color: var(--text-grey); font-size: 15px; margin-top: 2px; }
  .role-rule { width: 44px; height: 3px; background: var(--brand-blue); margin-top: 8px; }
  .contact { position: absolute; left: 50px; bottom: 70px; color: var(--text-grey); font-size: 15px; line-height: 1.55; }
  .contact-address { margin-bottom: 4px; }
  .contact-line { display: flex; align-items: center; gap: 10px; }
  .contact-line svg { width: 14px; height: 14px; flex: none; }
  .brand-name {
    position: absolute; right: 50px; bottom: 60px;
    color: var(--brand-blue); font-weight: 700; font-size: 30px;
  }
  .brand-name-reverse { color: var(--card-white); font-weight: 700; font-size: 48px; }
</style>
</head>
<body>
<main class="sheet">
  <section class="card card-front">
    <div class="identity">
      <p class="person-name">Dana Whitfield</p>
      <p class="person-role">Founder</p>
      <div class="role-rule"></div>
    </div>
    <div class="contact">
      <p class="contact-address">915 Mill Creek Rd<br>Norman, OK 73069</p>
      <p class="contact-line">
        <svg viewBox="0 0 16 16" aria-hidden="true"><path fill="var(--icon-blue)" d="M3.5 1.5l2.5 0 1 3.5-1.8 1.2a8 8 0 0 0 4.6 4.6L11 9l3.5 1v2.5c0 1-1 2-2 2A11 11 0 0 1 1.5 3.5c0-1 1-2 2-2z"/></svg>
        405.555.0142
      </p>
      <p class="contact-line">
        <svg viewBox="0 0 16 16" aria-hidden="true"><rect x="1" y="3" width="14" height="10" fill="var(--icon-blue)"/><path d="M1 3l7 5.5L15 3" fill="none" stroke="#fff" stroke-width="1.4"/></svg>
        contact@marlowsovenworks.com
      </p>
      <p class="contact-line">
        <svg viewBox="0 0 16 16" aria-hidden="true"><circle cx="8" cy="8" r="6.5" fill="none" stroke="var(--icon-blue)" stroke-width="1.5"/><ellipse cx="8" cy="8" rx="2.8" ry="6.5" fill="none" stroke="var(--icon-blue)" stroke-width="1.2"/><path d="M1.5 8h13M2.5 5h11M2.5 11h11" stroke="var(--icon-blue)" stroke-width="1.1"/></svg>
        www.marlowsovenworks.com
      </p>
    </div>
    <p class="brand-name">Marlow's Ovenworks</p>
  </section>

  <section class="card card-back">
    <p class="brand-name-reverse">Marlow's Ovenworks</p>
  </section>
</main>
</body>
</html>
```